meridale partners business card

Architectural firm business card
Updates

Please note:

corporate colour black+yellow are the only elements to be kept.
NO OTHER ELEMENT TO BE REUSED FROM PREVIOUS BUSINESS CARD.
Thank you.

Dear Everyone,

Thank you for your participation. I have upload the KBSO+ logo again for incoporate in the card. in tif and pdf format.

Thank you 

I keep getting request for the logo file. Does everyone has the same problem?

I cannot do much, because the file is upload to the website server. I can't seem to see it either.

The logo file is now working. Please download. I check it myself. Thank you everyone.

Dear All,

Thank you for all the hard work. There are a lot of great work. Due to current commitment with work, I am unable to review them just yet. I will do so next week and advise everyone also. Thank you again. Best regards

Dear All,

Thank you for your participation. There are a lot of good design. Unfortunately, I can only select one. All the best. This is definitely a good crowd to work with. Thank you everyone again.

Best regards

Target Market(s)

Corporate, commercial and institutional projects only

Industry/Entity Type

Business

Requirements
Must have
• elegant simple
double sided with coating
Member of Southland Guild of Draughtsmen (logo only)
corporate colour black and

LOGO FILE UPLOADED
Should not have
• should not be the same as current business card.
upload for reference information only.
font sans serif preferred.

```html
<!DOCTYPE html>
<html lang="en">
<head>
<meta charset="utf-8">
<title>Meridale Partners business card</title>
<link rel="stylesheet" href="https://fonts.googleapis.com/css2?family=Open+Sans:wght@400;600;700&display=swap">
<style>
  :root {
    --ink: #231f20;
    --amber: #f59f45;
    --paper: #ffffff;
    --stage: #e9e6e1;
    --muted: #d8d8d8;
  }
  * { margin: 0; padding: 0; box-sizing: border-box; }
  html, body { width: 1200px; height: 900px; overflow: hidden; }
  body {
    background: var(--stage);
    font-family: "Open Sans", Arial, sans-serif;
    position: relative;
  }
  .card {
    position: absolute;
    left: 250px;
    width: 700px;
    height: 400px;
    border-radius: 20px;
    overflow: hidden;
    background: var(--ink);
    box-shadow: 0 6px 18px rgba(0,0,0,0.25);
  }
  .card--back { top: 30px; }
  .card--front { top: 470px; }
  .card__shapes { position: absolute; inset: 0; }
  .brand {
    position: absolute;
    display: flex;
    align-items: center;
    gap: 14px;
    color: var(--paper);
    font-weight: 700;
    letter-spacing: 0.5px;
  }
  .brand__square { background: var(--paper); display: block; }
  .card--back .brand { left: 60px; top: 150px; font-size: 30px; }
  .card--back .brand__square { width: 44px; height: 44px; }
  .card--front .brand { left: 40px; top: 34px; font-size: 24px; }
  .card--front .brand__square { width: 36px; height: 36px; }
  .services {
    position: absolute;
    color: var(--paper);
    font-size: 20px;
    line-height: 1.25;
    letter-spacing: 0.5px;
  }
  .card--back .services { left: 390px; top: 48px; font-size: 23px; }
  .card--front .services { right: 36px; top: 36px; text-align: right; }
  .company {
    position: absolute;
    font-weight: 600;
    white-space: nowrap;
  }
  .card--back .company { right: 40px; top: 300px; color: var(--ink); }
  .card--back .company__main { font-size: 34px; }
  .card--back .company__suffix { font-size: 19px; }
  .card--front .company { right: 24px; top: 286px; color: var(--paper); }
  .card--front .company__main { font-size: 28px; }
  .card--front .company__suffix { font-size: 15px; }
  .person {
    position: absolute;
    left: 40px;
    top: 110px;
    color: var(--paper);
  }
  .person__name { font-size: 24px; font-weight: 700; }
  .person__post { font-size: 12px; font-weight: 600; margin-left: 6px; }
  .person__role { font-size: 14px; line-height: 1.3; margin-left: 10px; }
  .contacts {
    position: absolute;
    left: 30px;
    top: 224px;
    list-style: none;
    color: var(--ink);
    font-size: 14px;
  }
  .contacts li {
    display: flex;
    align-items: center;
    gap: 10px;
    height: 30px;
  }
  .contacts svg { width: 16px; height: 16px; fill: var(--paper); flex: none; }
  .web {
    position: absolute;
    right: 36px;
    top: 354px;
    color: var(--ink);
    font-size: 18px;
    letter-spacing: 0.3px;
  }
</style>
</head>
<body>

<section class="card card--back" aria-label="Card back">
  <svg class="card__shapes" viewBox="0 0 700 400" preserveAspectRatio="none">
    <polygon points="0,280 700,215 700,400 0,400" fill="var(--amber)"/>
  </svg>
  <div class="brand"><span class="brand__square"></span>meridale partners</div>
  <p class="services">architects<br>urban designers<br>project managers</p>
  <p class="company"><span class="company__main">Meridale partners</span> <span class="company__suffix">pty limited</span></p>
</section>

<section class="card card--front" aria-label="Card front">
  <svg class="card__shapes" viewBox="0 0 700 400" preserveAspectRatio="none">
    <polygon points="0,205 260,205 380,400 0,400" fill="var(--amber)"/>
    <polygon points="343,340 700,340 700,400 380,400" fill="var(--paper)"/>
    <polygon points="371,386 700,386 700,400 380,400" fill="var(--muted)"/>
  </svg>

  <div class="brand"><span class="brand__square"></span>meridale partners</div>
  <p class="services">architects<br>urban designers<br>project managers</p>

  <div class="person">
    <p><span class="person__name">Linh Baker</span><span class="person__post">kbso,sgd</span></p>
    <p class="person__role">Architect (NSW BoA reg no: 7312)<br>Director</p>
  </div>

  <ul class="contacts">
    <li><svg viewBox="0 0 24 24"><rect x="6" y="1" width="12" height="22" rx="2"/><rect x="8" y="4" width="8" height="12" fill="var(--amber)"/></svg>0400 555 012</li>
    <li><svg viewBox="0 0 24 24"><path d="M2 9c0-4 20-4 20 0v2h-5V9H7v2H2z"/><path d="M5 13h14l2 9H3z"/></svg>+612 5550 1986</li>
    <li><svg viewBox="0 0 24 24"><rect x="6" y="2" width="12" height="7"/><rect x="2" y="9" width="20" height="9" rx="2"/><rect x="6" y="15" width="12" height="7"/></svg>+612 5550 1621</li>
    <li><svg viewBox="0 0 24 24"><rect x="2" y="5" width="20" height="14"/><path d="M2 5l10 8 10-8" fill="none" stroke="var(--amber)" stroke-width="2"/></svg>mail@meridalepartners.com.au</li>
    <li><svg viewBox="0 0 24 24"><path d="M12 2L1 12h3v10h6v-6h4v6h6V12h3z"/></svg>14 Alder Lane Wren Park NSW 2190</li>
  </ul>

  <p class="company"><span class="company__main">Meridale partners</span> <span class="company__suffix">pty limited</span></p>
  <p class="web">www.meridalepartners.com.au</p>
</section>

</body>
</html>
```